Automotive component supplier needs a business card design

We need a business card design for our company called Velmar Global Components Ltd based in the UK. We are a supplier of interior and exterior components to premium car manufacturers such as Corvane Hale, Durrant Fyfe, Maxtorn and Valdessimo. We would like to see a modern business card design that uses the colour blue.

Target Market(s)

Premium automotive car manufacturers.

Industry/Entity Type

Automotive

Contact Information for Business Card

Company Name : Velmar Global Components Limited
Address: 17 Tamsey Yard, Upper Drisk, Warwick, CV31 8RJ, United Kingdom
Web Address : www.velmarparts-example.co.uk

Font styles to use
Other font styles liked:
• Helvetica

Colors
3176b5
0255a3
85acd3
cfdeed
cee9f5
85cae6
34a6d7
0692cd
9bcb3c

Requirements
Must have
• Clear company logo and a mixture of blue colours.
Nice to have
• A high quality modern image.
Should not have
• Multiple colours.

```html
<!DOCTYPE html>
<html lang="en">
<head>
<meta charset="utf-8">
<title>Velmar Global Components – Business Card</title>
<link rel="stylesheet" href="https://fonts.googleapis.com/css2?family=Arimo:wght@400&family=Open+Sans:wght@400&display=swap">
<style>
  :root {
    --blue-deep: #3176b5;
    --blue-mid: #5e93c6;
    --blue-light: #9dbedd;
    --blue-logo: #3176b5;
    --paper: #ffffff;
    --backdrop: #eceef0;
    --text-light: #ffffff;
  }
  * { box-sizing: border-box; margin: 0; padding: 0; }
  html, body { width: 1200px; height: 720px; overflow: hidden; }
  body {
    background: var(--backdrop);
    display: flex;
    align-items: center;
    justify-content: center;
    gap: 60px;
    font-family: "Open Sans", sans-serif;
  }
  .card {
    position: relative;
    width: 520px;
    height: 298px;
    border-radius: 3px;
    overflow: hidden;
    box-shadow: 0 6px 18px rgba(0,0,0,0.12);
  }
  .card--front {
    background: linear-gradient(180deg, var(--blue-light) 0%, var(--blue-mid) 55%, var(--blue-deep) 100%);
  }
  .brand {
    font-family: "Arimo", sans-serif;
    font-weight: 400;
    text-transform: uppercase;
    line-height: 1;
  }
  .card--front .brand {
    position: absolute;
    left: 42px;
    top: 78px;
    color: var(--text-light);
  }
  .card--front .brand-name {
    display: block;
    font-size: 92px;
    letter-spacing: 2px;
  }
  .card--front .brand-tag {
    display: block;
    margin-top: 14px;
    font-size: 25px;
    letter-spacing: 3.4px;
  }
  .card--back {
    background: linear-gradient(180deg, var(--blue-light) 0%, var(--blue-mid) 55%, var(--blue-deep) 100%);
  }
  .back-panel {
    position: absolute;
    inset: 0;
    background: var(--paper);
    clip-path: polygon(0 0, 30% 0, 47% 100%, 0 100%);
  }
  .card--back .brand {
    position: absolute;
    left: 22px;
    top: 30px;
    color: var(--blue-logo);
  }
  .card--back .brand-name {
    display: block;
    font-size: 30px;
    letter-spacing: 1px;
  }
  .card--back .brand-tag {
    display: block;
    margin-top: 5px;
    font-size: 8px;
    letter-spacing: 1px;
  }
  .address {
    position: absolute;
    right: 22px;
    top: 20px;
    text-align: right;
    font-style: normal;
    font-size: 11.5px;
    line-height: 1.35;
    color: var(--text-light);
  }
  .contact {
    position: absolute;
    right: 22px;
    bottom: 20px;
    text-align: right;
    font-size: 11.5px;
    line-height: 1.4;
    color: var(--text-light);
    list-style: none;
  }
  .contact li { display: flex; justify-content: flex-end; align-items: center; gap: 5px; }
  .contact svg { width: 10px; height: 11px; }
  .contact-rule {
    width: 36px;
    height: 1px;
    background: var(--text-light);
    margin: 7px 0 20px auto;
  }
</style>
</head>
<body>
  <section class="card card--front" aria-label="Business card front">
    <div class="brand">
      <span class="brand-name">Velmar</span>
      <span class="brand-tag">Global Components</span>
    </div>
  </section>

  <section class="card card--back" aria-label="Business card back">
    <div class="back-panel"></div>
    <div class="brand">
      <span class="brand-name">Velmar</span>
      <span class="brand-tag">Global Components</span>
    </div>
    <address class="address">
      17 Tamsey Yard, Upper Drisk,<br>
      Warwick, CV31 8RJ<br>
      United Kingdom
    </address>
    <ul class="contact">
      <li>
        <svg viewBox="0 0 10 12" aria-hidden="true"><rect x="1.5" y="0.5" width="7" height="11" rx="1.2" fill="none" stroke="#fff" stroke-width="1"/><line x1="4" y1="9.6" x2="6" y2="9.6" stroke="#fff" stroke-width="1"/></svg>
        +44 1926 000118
      </li>
      <li>
        <svg viewBox="0 0 12 12" aria-hidden="true"><path d="M2.6 0.8 L4.6 3.4 L3.4 4.8 Q4.6 7.4 7.2 8.6 L8.6 7.4 L11.2 9.4 L9.8 11.2 Q4.8 11 0.8 3 Z" fill="#fff"/></svg>
        +44 1926 000119
      </li>
      <li class="contact-rule" aria-hidden="true"></li>
      <li>hello@velmarparts-example.co.uk</li>
      <li>www.velmarparts-example.co.uk</li>
    </ul>
  </section>
</body>
</html>
```